Newsletter-Design für Garten-Samen Shop
Zielgruppe
Online Shop für Obst-, Gemüse-, Kräuter- und Pflanzensamen
Aufgabenstellung
www.beet-ratgeber-netz.de ist die Seite mit den Produkten. Als Tipp sollte das Jiaogulan genannt werden da dieses Produkt sich am meisten verkauft.

```html
<!DOCTYPE html>
<html lang="de">
<head>
<meta charset="utf-8">
<title>Beet Ratgeber Newsletter</title>
<link href="https://fonts.googleapis.com/css2?family=Allison&family=Arimo:wght@400;700&family=Nothing+You+Could+Do&display=swap" rel="stylesheet">
<style>
  :root {
    --green: #93c01f;
    --green-bright: #3cb043;
    --purple: #a86bb5;
    --ink: #111111;
    --script-grey: #4f4a52;
    --white: #ffffff;
    --dark-badge: #2f2f2f;
    --melon-a: #5d7f3a;
    --melon-b: #2e3a22;
    --herb-a: #8fbf4a;
    --herb-b: #4e7d2a;
    --chive-a: #8a6a4c;
    --chive-b: #cfc3ad;
  }
  * { box-sizing: border-box; margin: 0; padding: 0; }
  html, body { width: 1200px; height: 2600px; overflow: hidden; background: var(--white); }
  body { font-family: "Arimo", Arial, sans-serif; color: var(--ink); }
  .newsletter { position: relative; width: 1200px; height: 2600px; }
  .abs { position: absolute; }
  .script { font-family: "Allison", cursive; font-weight: 400; line-height: 1; white-space: nowrap; }

  .header-band { left: 0; top: 0; width: 1200px; height: 310px; background: var(--green); }
  .brand-name { left: 40px; top: 108px; color: var(--white); font-weight: 700; font-size: 42px; letter-spacing: -0.5px; }
  .brand-tagline { left: 40px; top: 162px; color: var(--white); font-weight: 700; font-size: 16px; }
  .masthead { left: 340px; top: 0; font-size: 270px; color: var(--script-grey); }

  .offer-title { left: 100px; top: 372px; font-size: 185px; color: var(--green-bright); }
  .offer-kicker { left: 206px; top: 414px; color: var(--purple); font-weight: 700; font-size: 28px; }
  .offer-text { left: 70px; top: 522px; width: 712px; text-align: center; font-size: 30px; line-height: 40px; }
  .btn { border: 2px solid #555; display: flex; align-items: center; justify-content: center; font-size: 29px; color: var(--ink); text-decoration: none; background: var(--white); }
  .btn-offer { left: 210px; top: 780px; width: 444px; height: 86px; }
  .offer-photo { left: 794px; top: 426px; width: 372px; height: 372px; border-radius: 50%; background: radial-gradient(circle at 45% 60%, var(--melon-a), var(--melon-b)); }

  .divider { left: 34px; width: 1132px; height: 3px; background: var(--green); }

  .tip-photo { left: 64px; top: 1072px; width: 488px; height: 324px; background: linear-gradient(135deg, var(--herb-a), var(--herb-b)); }
  .tip-badge { left: 40px; top: 960px; width: 244px; height: 244px; border-radius: 50%; background: var(--dark-badge); }
  .tip-badge-label { left: 30px; top: 1010px; width: 260px; text-align: center; font-size: 170px; color: var(--white); }
  .tip-title { left: 680px; top: 944px; font-size: 128px; color: var(--ink); }
  .tip-text { left: 576px; top: 1082px; width: 566px; font-size: 29px; line-height: 40px; text-align: justify; }
  .btn-tip { left: 616px; top: 1438px; width: 506px; height: 82px; }

  .chive-photo { left: 186px; top: 1630px; width: 854px; height: 400px; background: linear-gradient(160deg, var(--chive-a), var(--chive-b) 60%, var(--herb-b)); }
  .chive-band { left: 310px; top: 1714px; width: 730px; height: 116px; background: rgba(110,110,110,0.6); }
  .chive-title { left: 346px; top: 1694px; font-size: 165px; color: var(--white); }
  .chive-text { left: 110px; top: 2038px; width: 980px; text-align: center; font-size: 28px; line-height: 40px; }
  .btn-chive { left: 614px; top: 2232px; width: 510px; height: 72px; }

  .more-note { left: 72px; top: 2250px; width: 380px; z-index: 2; font-family: "Nothing You Could Do", cursive; font-size: 30px; line-height: 50px; transform: rotate(-14deg); transform-origin: left top; }
  .more-note span { display: block; }
  .more-note .last { padding-left: 130px; }

  .footer-band { left: 0; top: 2392px; width: 1200px; height: 208px; background: var(--green); }
  .footer-url { left: 0; top: 2468px; width: 1200px; text-align: center; color: var(--white); font-weight: 700; font-size: 46px; }
  .footer-links { left: 0; top: 2528px; width: 1200px; text-align: center; font-size: 30px; color: var(--ink); }
  .footer-links a { color: var(--ink); text-decoration: underline; text-decoration-color: var(--white); }
</style>
</head>
<body>
<main class="newsletter">
  <header>
    <div class="abs header-band"></div>
    <div class="abs brand-name">Beet Ratgeber</div>
    <div class="abs brand-tagline">Obst, Gemüse + Pflanzen</div>
    <h1 class="abs script masthead">Newsletter</h1>
  </header>

  <section class="offer">
    <div class="abs script offer-title">Wassermelone</div>
    <div class="abs offer-kicker">Diese Woche im ANGEBOT</div>
    <p class="abs offer-text">Lorem ipsum dolor sit amet, consetetur sadips&shy;cing elitr, sed diam nonumy eirmod tempor invid&shy;unt ut labore et dolore magna aliquyam erat, sed diam voluptua. At vero eos et accusam et justo duo dolores et ea rebum.</p>
    <a class="abs btn btn-offer" href="#">ZUM BEITRAG</a>
    <div class="abs offer-photo" role="img" aria-label="Foto einer Wassermelone auf dem Beet zwischen Blättern"></div>
  </section>

  <div class="abs divider" style="top:934px"></div>

  <section class="tip">
    <div class="abs tip-photo" role="img" aria-label="Foto von grünen Jiaogulan-Blättern"></div>
    <div class="abs tip-badge"></div>
    <div class="abs script tip-badge-label">Tipp</div>
    <h2 class="abs script tip-title">Jiaogulan</h2>
    <p class="abs tip-text">Das Kraut der Unsterblichkeit<br>Lorem ipsum dolor sit amet, consetet sadipscing elitr, sed diam nonumy eirmod tempor invidunt ut labore et dolore magna aliquyam erat, sed diam voluptua. At vero eos et accuet justo duo dolores et ea rebum. Stet clita kasd gubergren, no sea mata est</p>
    <a class="abs btn btn-tip" href="#">ZUM SHOP</a>
  </section>

  <div class="abs divider" style="top:1566px"></div>

  <section class="chives">
    <div class="abs chive-photo" role="img" aria-label="Foto von geschnittenem Schnittlauch auf einem Holzbrett mit Messer"></div>
    <div class="abs chive-band"></div>
    <h2 class="abs script chive-title">Schnittlauch</h2>
    <p class="abs chive-text">Lorem ipsum dolor sit amet, consetetur sadipscing elitr, sed diam nonumy eirmod tempor invidunt ut labore et dolore magna aliquyam erat, sed diam voluptua. At vero eos et accusam et justo duo dolores et ea rebum. Stet clita kasd gubergren, no sea takimata sanctus est</p>
    <a class="abs btn btn-chive" href="#">WEITER LESEN</a>
  </section>

  <footer>
    <div class="abs footer-band"></div>
    <div class="abs footer-url">www.beet-ratgeber-netz.de</div>
    <div class="abs footer-links"><a href="#">Mehr über uns</a> &nbsp;I <a href="#">Unsubscribe</a></div>
  </footer>

  <p class="abs more-note"><span>Noch mehr über</span><span>Kräuter, Obst &amp;</span><span>Gemüse zu finden</span><span class="last">auf…</span></p>
</main>
</body>
</html>
```